Brightpath Orthodontics business card design

Need a business card design that reflects our re-branding (orthodontic office - braces) and a new partnership with a pediatric dental office. We would like to include "for adults and children" on the card as well so adults know they are welcome to get their braces here as well. Office design is modern and would like business card to reflect a modern type look. Here's the text we would like to be included on the card:

Darren Holloway, DDS, MSD
5214 West Maple Avenue, Suite 204
Mansfield, TX 76099
817-555-0143
www.brightpathortho.example
info@brightpathortho.example
Updates

Can we add the following to the existing designs? Darren Holloway, DDS, MSD 5214 West Maple Avenue, Suite 204 Mansfield, TX 76099 817-555-0143

Does anyone have any more vertical designs available? Thanks!

Industry/Entity Type

Dental

```html
<!DOCTYPE html>
<html lang="en">
<head>
<meta charset="utf-8">
<title>Brightpath Orthodontics – Business Card</title>
<link rel="stylesheet" href="https://fonts.googleapis.com/css2?family=Open+Sans:wdth,wght@75..100,400..700&display=swap">
<style>
  :root {
    --page-bg: #e8e8e8;
    --card-bg: #ffffff;
    --ink: #111111;
    --credential: #8a2a16;
    --facet-orange: #f7941d;
    --facet-yellow: #f9ec23;
    --facet-blue: #1b75bc;
    --facet-green: #8dc63f;
    --facet-pink: #ec168c;
    --facet-plum: #9e1f63;
  }
  html, body {
    margin: 0;
    width: 1000px;
    height: 1200px;
    overflow: hidden;
    background: var(--page-bg);
  }
  .card {
    position: absolute;
    left: 248px;
    top: 195px;
    width: 483px;
    height: 825px;
    background: var(--card-bg);
    overflow: hidden;
    font-family: "Open Sans", Arial, sans-serif;
    font-stretch: 96%;
    color: var(--ink);
  }
  .facet-corner {
    position: absolute;
    left: 0;
    top: 0;
  }
  .brand {
    position: absolute;
    left: 54px;
    top: 352px;
    margin: 0;
  }
  .brand-name {
    margin: 0;
    font-size: 38px;
    font-weight: 700;
    line-height: 46px;
    color: var(--ink);
  }
  .audience {
    margin: 8px 0 0;
    font-size: 17px;
    font-weight: 400;
    line-height: 22px;
    color: var(--credential);
    white-space: nowrap;
  }
  .doctor {
    position: absolute;
    left: 54px;
    top: 548px;
    margin: 0;
    font-size: 29px;
    font-weight: 400;
    white-space: nowrap;
  }
  .doctor .credentials {
    font-size: 18px;
    color: var(--credential);
  }
  .contact {
    position: absolute;
    left: 54px;
    top: 649px;
    margin: 0;
    padding: 0;
    list-style: none;
    font-size: 18px;
    line-height: 25.5px;
  }
  .contact li {
    position: relative;
    padding-left: 27px;
    white-space: nowrap;
  }
  .contact .icon {
    position: absolute;
    left: 1px;
    top: 6px;
    width: 14px;
    height: 14px;
  }
</style>
</head>
<body>
  <main class="card">
    <svg class="facet-corner" width="483" height="825" viewBox="0 0 483 825" role="img" aria-label="Colourful faceted geometric pattern in the top right corner">
      <defs>
        <linearGradient id="facetTones" x1="0" y1="0" x2="1" y2="0.9">
          <stop offset="0" stop-color="var(--facet-orange)"/>
          <stop offset="0.3" stop-color="var(--facet-yellow)"/>
          <stop offset="0.5" stop-color="var(--facet-blue)"/>
          <stop offset="0.72" stop-color="var(--facet-pink)"/>
          <stop offset="0.88" stop-color="var(--facet-yellow)"/>
          <stop offset="1" stop-color="var(--facet-orange)"/>
        </linearGradient>
      </defs>
      <path d="M62,0 L483,0 L483,625 C450,380 300,140 62,0 Z" fill="url(#facetTones)"/>
    </svg>

    <header class="brand">
      <h1 class="brand-name">Brightpath<br>Orthodontics</h1>
      <p class="audience">for adults and children</p>
    </header>

    <p class="doctor">Darren Holloway, <span class="credentials">DDS, MSD</span></p>

    <ul class="contact">
      <li>
        <svg class="icon" viewBox="0 0 14 14" aria-hidden="true"><circle cx="7" cy="7" r="6" fill="none" stroke="currentColor" stroke-width="1.2"/><path d="M7 3.3a2 2 0 0 1 2 2c0 1.5-2 4-2 4s-2-2.5-2-4a2 2 0 0 1 2-2z" fill="currentColor"/></svg>
        5214 West Maple Avenue, Suite 204<br>Mansfield, TX 76099
      </li>
      <li>
        <svg class="icon" viewBox="0 0 14 14" aria-hidden="true"><circle cx="7" cy="7" r="6" fill="none" stroke="currentColor" stroke-width="1.2"/><path d="M4.6 3.8l1.3-.3.8 1.7-.8.7c.4.9 1 1.5 1.9 1.9l.7-.8 1.7.8-.3 1.3c-2.8.2-5.4-2.4-5.3-5.3z" fill="currentColor"/></svg>
        817-555-0143
      </li>
      <li>
        <svg class="icon" viewBox="0 0 14 14" aria-hidden="true"><g fill="none" stroke="currentColor" stroke-width="1.1"><circle cx="7" cy="7" r="6"/><ellipse cx="7" cy="7" rx="2.6" ry="6"/><path d="M1 7h12M2 4h10M2 10h10"/></g></svg>
        www.brightpathortho.example
      </li>
      <li>
        <svg class="icon" viewBox="0 0 14 14" aria-hidden="true"><g fill="none" stroke="currentColor" stroke-width="1.2"><circle cx="7" cy="7" r="6"/><circle cx="7" cy="7" r="3.4"/><circle cx="7" cy="7" r="1.1" fill="currentColor"/></g></svg>
        info@brightpathortho.example
      </li>
    </ul>
  </main>
</body>
</html>
```